Flyer/Poster design required for volunteer activities

We need a STRIKING A4 Poster/Flyer advertising our conservation volunteer program activities which are currently happening in the area. This poster is to advertise the program once people have arrived on the island or to locals. The program covers 5 months, May-September 2019 and is focused on conservation. I have attached the following:
- a flyer which was previously created (Tidewatch Habitat Helpers 2019 sm)to advertise the program - would prefer it has a similar striking resemblance, but not essential
- A mock up document 'TWHH On Island Poster_2019_v2' with text -Logos-Images

Target Market(s)

Everyone interested in Environmental Adventure/Hiking/Citizen Science

Industry/Entity Type

Tourism

Font styles to use
Sans Serif

Requirements
Must have
• -A travel conservation focus
• -Must use 'LHI-Background Image' as the background to the design
• -The info of where to get more information and the social media details must be prominent

```html
<!DOCTYPE html>
<html lang="en">
<head>
<meta charset="utf-8">
<title>Lord Howe Island – Tidewatch Habitat Helpers 2019</title>
<link href="https://fonts.googleapis.com/css2?family=Dosis:wght@300;400;500&display=swap" rel="stylesheet">
<style>
  :root{
    --magenta:#e81ec8;
    --green:#93c41c;
    --orange:#f0671c;
    --purple:#8e52c9;
    --amber:#e39a12;
    --teal:#1fd3a0;
    --ink:#0e0e12;
    --white:#ffffff;
    --soft:#f3f3e8;
  }
  *{margin:0;padding:0;box-sizing:border-box}
  html,body{width:849px;height:1200px;overflow:hidden;background:#fff}
  body{font-family:"Dosis",sans-serif;color:var(--white)}
  .poster{position:relative;width:849px;height:1200px;overflow:hidden}

  .backdrop{position:absolute;inset:0;
    background:
      radial-gradient(ellipse 300px 160px at 620px 190px,#8a6a5a 0%,rgba(138,106,90,0) 100%),
      radial-gradient(ellipse 420px 260px at 200px 900px,rgba(170,140,70,.8) 0%,rgba(170,140,70,0) 100%),
      linear-gradient(180deg,#d9e6ec 0%,#b7c9d2 10%,#5c8fb0 22%,#2b88b8 38%,#2a6f9c 52%,#6b7a52 66%,#8a7a3c 78%,#3d3a22 90%,#1b1a12 100%);}

  .banner{position:absolute;left:0;top:37px;width:849px;height:133px;
    background:linear-gradient(90deg,var(--magenta) 0%,rgba(232,30,200,.85) 45%,rgba(190,60,200,.35) 75%,rgba(190,60,200,0) 100%)}
  .title{position:absolute;left:46px;top:52px;font-size:62px;font-weight:400;letter-spacing:0.5px;line-height:1}
  .tagline{position:absolute;left:46px;top:118px;font-size:29px;font-weight:400;letter-spacing:2px;line-height:1}

  .badge{position:absolute;left:676px;top:36px;width:132px;height:132px;border-radius:50%;
    background:var(--white);border:5px solid #2a66c9;display:flex;align-items:center;justify-content:center;
    text-align:center;color:#2a66c9;font-size:16px;font-weight:500;line-height:1.15;padding:14px}

  .band{position:absolute;height:var(--h)}
  .band.left{left:130px;width:700px;padding-left:104px;padding-top:14px}
  .band.right{left:140px;width:540px;padding-right:60px;padding-top:14px;text-align:right}
  .band h2{font-size:21.5px;font-weight:500;line-height:1.2;letter-spacing:.2px}
  .band .week{font-size:16px;font-weight:400;margin-top:4px}
  .band p{font-size:12.6px;font-weight:300;line-height:15.5px;margin-top:6px;color:var(--soft)}

  .birds{top:210px;--h:132px;background:linear-gradient(90deg,var(--green) 0%,var(--green) 70%,rgba(147,196,28,0) 100%)}
  .marine{top:386px;--h:126px;background:linear-gradient(270deg,var(--orange) 0%,var(--orange) 65%,rgba(240,103,28,0) 100%)}
  .invasive{top:552px;--h:132px;background:linear-gradient(90deg,var(--purple) 0%,var(--purple) 70%,rgba(142,82,201,0) 100%)}
  .inverts{top:718px;--h:130px;background:linear-gradient(270deg,var(--amber) 0%,var(--amber) 65%,rgba(227,154,18,0) 100%)}
  .paradise{top:888px;--h:140px;background:linear-gradient(90deg,var(--teal) 0%,var(--teal) 70%,rgba(31,211,160,0) 100%)}

  .photo{position:absolute;width:176px;height:176px;border-radius:50%;border:6px solid var(--ring)}
  .photo.bird{left:40px;top:188px;--ring:var(--green);background:radial-gradient(circle at 45% 45%,#9a9a9c,#5d6a4a 70%,#3b4a2a)}
  .photo.diver{left:640px;top:350px;--ring:var(--orange);background:radial-gradient(circle at 50% 45%,#3a4a6a,#5fb6d8 70%,#8fd3e8)}
  .photo.forest{left:40px;top:530px;--ring:var(--purple);background:radial-gradient(circle at 50% 50%,#6f8a4a,#3d5a2a 70%,#28381c)}
  .photo.stick{left:640px;top:702px;--ring:var(--amber);background:radial-gradient(circle at 50% 50%,#4a4448,#d8b7a6 60%,#e9dfd8)}
  .photo.hiker{left:40px;top:868px;--ring:var(--teal);background:linear-gradient(180deg,#dfe9f2 0%,#a9c3dc 40%,#3f8fb0 58%,#4a6a3a 78%,#2c3a20 100%)}

  .footer{position:absolute;left:0;top:1084px;width:849px;height:116px;background:var(--ink);padding:10px 0 0 39px}
  .footer h3{font-size:26.5px;font-weight:400;letter-spacing:.4px;line-height:1.2}
  .footer .info{font-size:17px;font-weight:400;margin-top:6px}
  .social{display:flex;align-items:center;gap:8px;font-size:17px;margin-top:7px}
  .social .dot{width:15px;height:15px;border-radius:50%;background:var(--white);display:inline-block}
  .social .item{display:flex;align-items:center;gap:6px;margin-right:8px}
</style>
</head>
<body>
<div class="poster">
  <div class="backdrop" role="img" aria-label="Aerial photo of Lord Howe Island lagoon, mountains and coastline"></div>

  <div class="banner"></div>
  <h1 class="title">LORD HOWE ISLAND</h1>
  <div class="tagline">BE INVOLVED IN PROTECTING PARADISE...</div>
  <div class="badge">Tidewatch Habitat Helpers</div>

  <section class="band left birds">
    <h2>MAY 2019: BIRDS OF LORD HOWE ISLAND</h2>
    <div class="week">FEATURE WEEK: 19th - 26th May</div>
    <p>Ocean bird watching boat trips • Guided tours of Woodhen and<br>Currawong quarters • Weekly lectures at the Lord Howe Island<br>Museum • Weekly screenings of documentaries on Bird and Island<br>Conservation projects • Self guided land bird survey tours.</p>
  </section>
  <div class="photo bird" role="img" aria-label="Photo of a grey seabird chick"></div>

  <section class="band right marine">
    <h2>JUNE 2019: LORD HOWE ISLAND MARINE PARK</h2>
    <div class="week">FEATURE WEEK: 3rd - 9th June</div>
    <p>Marine pest monitoring with marine park staff • Marine plastic &amp; debris<br>clean up activities • Screenings of marine conservation documentaries<br>at the museum • Weekly lectures on Marine Life at the Lord Howe<br>Island Museum • Marine Activities with local operators.</p>
  </section>
  <div class="photo diver" role="img" aria-label="Photo of a snorkeller recording an underwater survey"></div>

  <section class="band left invasive">
    <h2>JULY 2019: INVASIVE SPECIES</h2>
    <div class="week">FEATURE WEEK: 21st - 28th July</div>
    <p>Guided walks to learn about the weed eradication program •<br>Weekly lectures on plants of Lord Howe Island • Weekly screenings of<br>documentaries on plant and island conservation projects • Guided walks<br>to Mount Gower • Local tour guides include commentaries on island plants.</p>
  </section>
  <div class="photo forest" role="img" aria-label="Photo of a hiker on a forest track among palms"></div>

  <section class="band right inverts">
    <h2>AUGUST 2019: AMAZING INVERTEBRATES</h2>
    <div class="week">FEATURE WEEK: 11th - 19th August</div>
    <p>Guided night walks to learn about the island's invertebrates • Weekly viewing<br>and presentation of the Lord Howe Island Phasmid • Weekly lectures on<br>invertebrates of Lord Howe Island at the museum • Weekly screenings of<br>documentaries on island conservation projects.</p>
  </section>
  <div class="photo stick" role="img" aria-label="Photo of a stick insect held in open hands"></div>

  <section class="band left paradise">
    <h2>SEPTEMBER 2019: PROTECTING PARADISE</h2>
    <div class="week">FEATURE WEEK: 1st - 8th September</div>
    <p>Observational snorkel surveys with Marine Ecologists, to assess populations<br>of McCulloch's Anemonefish and other unique fish species • Guided snorkel<br>and glass bottom boat tour to assess coral health within the Lord Howe Island<br>Marine Park • Guided walks to learn about the island's conservation history.</p>
  </section>
  <div class="photo hiker" role="img" aria-label="Photo of a hiker on a summit overlooking the lagoon"></div>

  <footer class="footer">
    <h3>JOIN THE TIDEWATCH HABITAT HELPERS PROGRAM 2019</h3>
    <div class="info">See the LHI visitor centre for more information.</div>
    <div class="social">
      <span>FOLLOW US!</span>
      <span class="item"><span class="dot"></span>www.tidewatchhelpers.org</span>
      <span class="item"><span class="dot"></span>photos@twhh</span>
    </div>
  </footer>
</div>
</body>
</html>
```